IT Service Provider

We need a website which reflects the IT Services we can offer to small and mid-size companies. This reaches from LAN/WAN, Security, VoIP, WiFi, Storage, Penetration testing.and Support.

In addition to that, a Logo is needed and should be embedded in the website.

Company is registered in the UK under:
Pellwick Ltd
Company No. 05927318

Industry/Entity Type

Security

```html
<!DOCTYPE html>
<html lang="en">
<head>
<meta charset="utf-8">
<title>Pellwick Ltd – IT Services</title>
<link rel="stylesheet" href="https://fonts.googleapis.com/css2?family=Open+Sans:ital,wght@0,400;0,600;0,700;1,400&family=Arimo:wght@400;700&display=swap">
<style>
:root{
  --blue:#0f6bb6;
  --blue-dark:#0a4f8f;
  --green:#13a651;
  --navy:#0b1a2c;
  --text:#2b2b2b;
  --muted:#555;
  --line:#c9c9c9;
  --footer:#3b3b3b;
  --footer-out:#2e2e2e;
  --icon:#4d4d4d;
}
*{box-sizing:border-box;margin:0;padding:0}
html,body{width:970px;height:1200px;overflow:hidden;background:#fff}
body{font-family:"Arimo",Arial,sans-serif;color:var(--text)}
.canvas{position:relative;width:970px;height:1200px;overflow:hidden;border-top:2px solid var(--blue)}
.abs{position:absolute}
/* header */
.brand{left:144px;top:22px;display:flex;align-items:center;gap:8px}
.brand-dot{width:28px;height:28px;border-radius:50%;background:var(--blue)}
.brand-name{font-family:"Open Sans",sans-serif;font-weight:700;font-size:21px;color:var(--green);letter-spacing:.2px}
.search{left:530px;top:26px;width:150px;height:22px;border:1px solid #d4d4d4;font-family:"Open Sans",sans-serif;font-style:italic;font-size:9px;color:#666;padding:5px 6px}
.search svg{position:absolute;right:6px;top:4px}
.call{left:700px;top:20px;display:flex;gap:6px;align-items:center;font-family:"Open Sans",sans-serif}
.call small{display:block;font-size:9.5px;color:#333;line-height:11px}
.call strong{display:block;font-size:15px;font-weight:400;color:#222;line-height:18px}
.nav{left:390px;top:64px;display:flex;font-family:"Open Sans",sans-serif;font-size:10.5px;color:#333;text-transform:uppercase}
.nav a{padding:0 12px;border-left:1px solid #999;line-height:14px;color:inherit;text-decoration:none}
.nav a:first-child{border:0;color:var(--blue);font-weight:700}
/* hero */
.hero{left:0;top:94px;width:970px;height:341px;background:var(--navy)}
.hero-photo{left:136px;top:94px;width:699px;height:341px;background:radial-gradient(ellipse at 50% 45%,#a9c3dc 0%,#5b7fa6 35%,#1e3a5e 75%,#10233d 100%)}
.hero-arrow{width:30px;height:30px;border-radius:50%;background:rgba(10,20,30,.75);top:237px}
.hero-arrow svg{margin:9px}
.tagline{left:0;top:397px;width:970px;height:38px;background:var(--blue);border-top:1px solid #3f8fd0;border-bottom:1px solid var(--blue-dark)}
.tagline-inner{position:absolute;left:136px;width:699px;height:36px;background:#2a7fc4;color:#fff;font-family:"Open Sans",sans-serif;font-size:18.5px;text-align:center;line-height:36px}
/* section headings */
.heading{font-family:"Open Sans",sans-serif;font-weight:600;font-size:16.5px;color:var(--blue);border-bottom:1px dashed #a9a9a9;padding-bottom:3px}
.pager{display:flex;gap:10px}
/* services */
.service{top:512px;width:120px;text-align:center}
.service h3{font-family:"Open Sans",sans-serif;font-weight:400;font-size:11px;color:#333;margin-bottom:10px}
.service.active h3{color:var(--green);font-weight:600}
.ring{width:98px;height:98px;margin:0 auto;border-radius:50%;background:radial-gradient(circle at 50% 40%,#f7f7f7,#dedede);border:2px solid #e2e2e2;box-shadow:0 0 0 2px #f3f3f3 inset;display:flex;align-items:center;justify-content:center}
.service.active .ring{border:3px solid var(--green);background:#fff}
.ring-shadow{width:70px;height:5px;margin:4px auto 11px;border-radius:50%;background:radial-gradient(#d6d6d6,transparent 70%)}
.service p{font-size:9.5px;line-height:14px;color:#222}
.divider{left:143px;top:709px;width:690px;height:1px;background:linear-gradient(90deg,transparent,#ddd 15%,#ddd 85%,transparent)}
/* columns */
.col{top:741px}
.about-photo{width:206px;height:95px;margin-top:11px;background:linear-gradient(180deg,#dfe6ee,#8c98a8 60%,#3b4150)}
.body-text{font-size:9.4px;line-height:12px;color:#333;text-align:justify}
.more{display:block;text-align:right;font-size:9px;font-weight:700;color:var(--green);margin-top:4px}
.quote{font-size:9.5px;line-height:15px;color:#333}
.q{font-family:Georgia,serif;font-weight:700;font-size:14px;line-height:0;color:#333}
.cite{display:block;text-align:right;font-size:8.5px;font-weight:700;color:#555;margin:2px 0 10px}
.field{width:207px;height:21px;border:1px solid #bfbfbf;box-shadow:inset 0 1px 2px #e5e5e5;font-family:"Open Sans",sans-serif;font-style:italic;font-size:8.5px;color:#666;padding:3px 8px;margin-bottom:12px}
.field.tall{height:61px}
.submit{width:51px;height:18px;background:var(--green);color:#fff;font-family:"Open Sans",sans-serif;font-weight:700;font-size:10px;text-align:center;line-height:18px}
/* clients */
.clients{position:absolute;left:143px;top:1045px;width:686px;display:flex;justify-content:space-between;align-items:center}
.client{display:flex;align-items:center;gap:5px;font-family:"Open Sans",sans-serif;font-weight:700;font-size:17px;color:#555}
.client i{display:block;width:14px;height:14px;background:#9a9a9a}
/* footer */
.footer-band{left:0;top:1113px;width:970px;height:87px;background:var(--footer-out)}
.footer{left:136px;top:1113px;width:699px;height:87px;background:var(--footer);border-top:2px solid #555}
.fnav{left:8px;top:14px;display:flex;gap:14px;font-size:9px;color:#eee}
.fnav span:first-child{color:var(--green)}
.faddr{left:8px;top:40px;font-size:8.5px;color:#eee;letter-spacing:.4px;line-height:17px}
.faddr div{display:flex;align-items:center;gap:6px}
.connect{left:366px;top:14px;font-family:"Open Sans",sans-serif;font-weight:600;font-size:10px;color:#fff}
.social{left:367px;top:40px;display:flex;gap:7px}
.social span{width:15px;height:15px;background:#8a8a8a;border-radius:2px}
.fmark{left:576px;top:10px;width:62px;height:42px;border-radius:50%;background:#5a5a5a}
.copy{left:527px;top:61px;font-size:8.5px;color:#eee;letter-spacing:.3px}
</style>
</head>
<body>
<div class="canvas">

  <header>
    <div class="abs brand"><span class="brand-dot"></span><span class="brand-name">Pellwick Ltd</span></div>
    <div class="abs search">search
      <svg width="11" height="11" viewBox="0 0 11 11"><circle cx="4.5" cy="4.5" r="3.5" fill="none" stroke="#888" stroke-width="1.3"/><line x1="7" y1="7" x2="10.5" y2="10.5" stroke="#888" stroke-width="1.5"/></svg>
    </div>
    <div class="abs call">
      <svg width="26" height="26" viewBox="0 0 26 26"><circle cx="13" cy="13" r="11.5" fill="none" stroke="var(--green)" stroke-width="2"/><path d="M9 7c1-1 2 0 2.5 1.5s-1 2-.5 3 2 3 3 3.5 1.5-1 3-.5 2 1.5 1 2.5-3 1.5-5.5-.5S6 9 9 7z" fill="var(--green)"/></svg>
      <div><small>Call Us Today</small><strong>020 7946 0321</strong></div>
    </div>
    <nav class="abs nav"><a>Home</a><a>About Us</a><a>Services</a><a>Testimonials</a><a>Clients</a><a>Contact Us</a></nav>
  </header>

  <section>
    <div class="abs hero"></div>
    <div class="abs hero-photo" role="img" aria-label="Photo of a businessman in a server room surrounded by glowing communication icons"></div>
    <div class="abs hero-arrow" style="left:146px"><svg width="12" height="12" viewBox="0 0 12 12"><path d="M8 1L3 6l5 5" fill="none" stroke="#fff" stroke-width="1.4"/></svg></div>
    <div class="abs hero-arrow" style="left:795px"><svg width="12" height="12" viewBox="0 0 12 12"><path d="M4 1l5 5-5 5" fill="none" stroke="#fff" stroke-width="1.4"/></svg></div>
    <div class="abs tagline"><div class="tagline-inner">WE HAVE SPECIALISED ENGINEERS TO DO SPECIALISED WORK</div></div>
  </section>

  <section>
    <h2 class="abs heading" style="left:145px;top:465px;width:686px">Our Services</h2>
    <div class="abs pager" style="left:798px;top:474px">
      <svg width="8" height="12" viewBox="0 0 8 12"><path d="M6 1L1 6l5 5" fill="none" stroke="#777" stroke-width="1.3"/></svg>
      <svg width="8" height="12" viewBox="0 0 8 12"><path d="M2 1l5 5-5 5" fill="none" stroke="var(--green)" stroke-width="1.3"/></svg>
    </div>

    <div class="abs service active" style="left:141px"><h3>Lanwan</h3>
      <div class="ring"><svg width="50" height="46" viewBox="0 0 50 46" fill="none" stroke="var(--icon)" stroke-width="4"><rect x="18" y="2" width="14" height="11"/><path d="M25 13v8M9 21h32M9 21v10M41 21v10"/><rect x="2" y="31" width="14" height="12"/><rect x="34" y="31" width="14" height="12"/></svg></div>
      <div class="ring-shadow"></div><p>Lorem ipsum dolor sit amet<br>ummy nibh eui smod</p></div>

    <div class="abs service" style="left:282px"><h3>Security</h3>
      <div class="ring"><svg width="40" height="46" viewBox="0 0 40 46"><path d="M20 2l17 6v14c0 11-8 19-17 22C11 41 3 33 3 22V8z" fill="var(--icon)"/><path d="M20 7l12 4v11c0 8-6 14-12 17-6-3-12-9-12-17V11z" fill="#e9e9e9"/><path d="M11 26l13-13M14 32l16-16M19 36l12-12" stroke="var(--icon)" stroke-width="3"/></svg></div>
      <div class="ring-shadow"></div><p>Lorem ipsum dolor sit amet<br>ummy nibh eui smod</p></div>

    <div class="abs service" style="left:424px"><h3>VoIP</h3>
      <div class="ring"><svg width="58" height="36" viewBox="0 0 58 36" fill="var(--icon)"><path d="M2 12C8 2 50 2 56 12l-2 6-10-2v-5c-8-3-22-3-30 0v5L4 18z"/><path d="M15 16h28l8 12v6H7v-6z"/><circle cx="29" cy="25" r="5" fill="#e6e6e6"/></svg></div>
      <div class="ring-shadow"></div><p>Lorem ipsum dolor sit amet<br>ummy nibh eui smod</p></div>

    <div class="abs service" style="left:565px"><h3>WiFi</h3>
      <div class="ring"><svg width="50" height="40" viewBox="0 0 50 40" fill="none" stroke="var(--icon)" stroke-width="5" stroke-linecap="round"><path d="M4 13a30 30 0 0 1 42 0M11 20a20 20 0 0 1 28 0M18 27a10 10 0 0 1 14 0"/><circle cx="25" cy="34" r="2.5" fill="var(--icon)"/></svg></div>
      <div class="ring-shadow"></div><p>Lorem ipsum dolor sit amet<br>ummy nibh eui smod</p></div>

    <div class="abs service" style="left:706px"><h3>Storage</h3>
      <div class="ring"><svg width="46" height="48" viewBox="0 0 46 48" fill="var(--icon)"><ellipse cx="23" cy="8" rx="21" ry="7"/><path d="M2 13c4 5 38 5 42 0v8c-4 5-38 5-42 0z"/><path d="M2 26c4 5 38 5 42 0v8c-4 5-38 5-42 0z"/><path d="M2 39c4 5 38 5 42 0v2c0 4-10 7-21 7S2 45 2 41z"/></svg></div>
      <div class="ring-shadow"></div><p>Lorem ipsum dolor sit amet<br>ummy nibh eui smod</p></div>

    <div class="abs divider"></div>
  </section>

  <section class="abs col" style="left:143px;width:207px">
    <h2 class="heading">About Pellwick Ltd.</h2>
    <div class="about-photo" role="img" aria-label="Photo of a business team smiling in a meeting"></div>
    <p class="body-text" style="margin-top:6px">Lorem Nonummy nibh uismod tincidunt ut laoreet olore magna aliquam erat volutpat. Ut wisi enim adinim nonummy nibh euismod tincidunt Nonummy nibh uismod tincidunt ut laoreet dolore magna aliquam erat volutpat. Ut wdreisi enim ad adinim nonummy nibh euismod tincidun Lorem Nonummy.</p>
    <span class="more">Read More »</span>
  </section>

  <section class="abs col" style="left:380px;width:208px">
    <h2 class="heading">Client Testimonials</h2>
    <p class="quote" style="margin-top:10px"><span class="q">“</span> Nonummy nibh uismod tincidunt ut laoreet dolore magna aliquam erat volutpat. Ut wisi enim ad minim nonummy nibh euismod tincidunt <span class="q">”</span></p>
    <span class="cite">Daniel Hart</span>
    <p class="quote"><span class="q">“</span> Nonummy nibh uismod tincidunt ut laoreet olore magna aliquam erat volutpat. Ut wisi enim adinim nonummy nibh euismod tincidunt Nonummy nibh uismod tincidunt ut laoreet dolore magna aliquam erat volutpat. Ut wisi enim ad minim nonummy nibh lorem tincidunt <span class="q">”</span></p>
    <span class="cite">Owen Marsh</span>
    <span class="more">Read More »</span>
  </section>

  <section class="abs col" style="left:620px;width:208px">
    <h2 class="heading">Quick Contact</h2>
    <div style="margin-top:10px">
      <div class="field">Name</div>
      <div class="field">Email</div>
      <div class="field">Phone</div>
      <div class="field tall">Message</div>
      <div class="submit">Submit</div>
    </div>
  </section>

  <section>
    <h2 class="abs heading" style="left:143px;top:996px;width:688px">Our Clients</h2>
    <div class="abs pager" style="left:798px;top:1005px">
      <svg width="8" height="12" viewBox="0 0 8 12"><path d="M6 1L1 6l5 5" fill="none" stroke="#777" stroke-width="1.3"/></svg>
      <svg width="8" height="12" viewBox="0 0 8 12"><path d="M2 1l5 5-5 5" fill="none" stroke="var(--green)" stroke-width="1.3"/></svg>
    </div>
    <div class="clients">
      <span class="client"><i></i>Norvane</span>
      <span class="client"><i></i>Kestrix</span>
      <span class="client">Altura</span>
      <span class="client">Corvell</span>
      <span class="client"><i></i>Kestrix</span>
      <span class="client">Altura</span>
    </div>
  </section>

  <footer>
    <div class="abs footer-band"></div>
    <div class="abs footer">
      <div class="abs fnav"><span>Home</span><span>About Us</span><span>Services</span><span>Testimonials</span><span>Clients</span><span>Contact Us</span></div>
      <div class="abs faddr">
        <div>Street Name, City Name State Zip code</div>
        <div>
          <svg width="10" height="10" viewBox="0 0 10 10"><path d="M2 0c1 0 2 2 2 3s-1 1-.5 2 1.5 2 2.5 1.5 1-1 2-.5 2 1.5 1.5 2.5S7 10 4 7 0 1 2 0z" fill="#eee"/></svg>020 7946 0321
          <svg width="11" height="8" viewBox="0 0 11 8" style="margin-left:4px"><rect width="11" height="8" fill="#eee"/><path d="M0 0l5.5 4.5L11 0" fill="none" stroke="#3b3b3b" stroke-width="1"/></svg>inquiry@pellwick.co.uk
        </div>
      </div>
      <div class="abs connect">Connect Us On</div>
      <div class="abs social" aria-label="Social media links"><span></span><span></span><span></span><span></span></div>
      <div class="abs fmark"></div>
      <div class="abs copy">© 2014 Pellwick. All Rights Reserved</div>
    </div>
  </footer>

</div>
</body>
</html>
```